verdant terraces simple classy business card design

my name is owen harlow and I run a gardening business aimed at high class verdant terraces. the business name is verdant terraces and our logo was designed on pixel forum .My clientel are anything from residential homes to businesses. I take pride in my work and know that I offer a service like no other in my area.
The business card will be used to represent my business and I want it to be not only rememberable, but simplistic and modern. Eye catching too. Of course I would like it relatable to gardening and appealing to the correct clientel - those being garden enthusiasts, prestigious homes and businesses that are after top of the line gardening services like no other on the market.
I am not a typical lawn mowing business so I don't want a typical card design that represents that. The gardens I work with are generally million dollar properties with owners who are very garden proud looking for upkeep and guidance from me along with sometimes whole new garden designs. I want the business cards to show to my clients that I take pride, as they do, in their garden. And I want them to know from my card that I am a professional, qualified horticulturist offering them a top of the line service for life. I want them to refer my business on. I want them to look at my business card and see class and professionalism in a modern unique bold way.
The card should be simple with the possibility of the logo on the front being embossed/debossed and my details on the back the card should have a organic garden feel it's very important to me that it is absolutely perfect
I am also very open to ideas and suggestions so look forward to seeing the designs. the business logo has been supplied with this project and I want the card to be double sided

Contact info is
Owen Harlow - Managing Director / Horticulturist
Phone : 0481 526 704
Email: owenharlow@verdantterraces.com.au

Target Market(s)

high class gardens residential and commercial

Industry/Entity Type

Gardener

Contact Information for Business Card

Contact info is
Phone : 0481 526 704

PLEASE MAKE CARD DOUBLE SIDED

Requirements
Must have
• organic simple classy modern feel
• must flow with the current logo that has been supplied with this project
• Double sided
• Must explain in a simple way that I deal with high end gardens and I'm a qualified horticulturist
Nice to have
• embossed debossed logo
Should not have
• shouldn't be to busy or cheap looking

```html
<!DOCTYPE html>
<html lang="en">
<head>
<meta charset="utf-8">
<title>Verdant Terraces — Business Card</title>
<link rel="stylesheet" href="https://fonts.googleapis.com/css2?family=Nunito+Sans:wght@300;400;600&display=swap">
<style>
  :root {
    --leaf: #5f9a4f;
    --paper: #ffffff;
    --ink: #2b2b2b;
    --backdrop: #c4c4c4;
    --card-w: 440px;
    --card-h: 770px;
  }
  * { box-sizing: border-box; margin: 0; padding: 0; }
  html, body {
    width: 1200px;
    height: 1200px;
    overflow: hidden;
    background: var(--backdrop);
    font-family: "Nunito Sans", sans-serif;
  }
  .sheet {
    width: 1200px;
    height: 1200px;
    display: flex;
    align-items: center;
    justify-content: center;
    gap: 60px;
  }
  .card {
    width: var(--card-w);
    height: var(--card-h);
    position: relative;
    overflow: hidden;
    box-shadow: 0 6px 18px rgba(0, 0, 0, 0.12);
  }

  /* Brand name block */
  .brand {
    display: flex;
    flex-direction: column;
    align-items: center;
    color: var(--paper);
    font-weight: 400;
    text-transform: uppercase;
    line-height: 1;
  }
  .brand__dot {
    width: 84px;
    height: 84px;
    border-radius: 50%;
    background: var(--paper);
    margin-bottom: 22px;
  }
  .brand__name {
    text-align: center;
  }
  .brand__name span { display: block; }

  /* Front */
  .card--front {
    background: var(--leaf);
    display: flex;
    align-items: center;
    justify-content: center;
  }
  .card--front .brand__name { font-size: 52px; letter-spacing: 0.06em; }
  .card--front .brand__name span + span { font-size: 26px; letter-spacing: 0.62em; margin-top: 12px; padding-left: 0.62em; }

  /* Back */
  .card--back { background: var(--paper); }
  .card__band {
    height: 306px;
    background: var(--leaf);
    display: flex;
    align-items: center;
    justify-content: center;
    padding-top: 18px;
  }
  .card--back .brand__dot { width: 62px; height: 62px; margin-bottom: 16px; }
  .card--back .brand__name { font-size: 38px; letter-spacing: 0.05em; }
  .card--back .brand__name span + span { font-size: 19px; letter-spacing: 0.62em; margin-top: 8px; padding-left: 0.62em; }

  .contact {
    display: flex;
    flex-direction: column;
    align-items: center;
    text-align: center;
    color: var(--ink);
    padding-top: 52px;
  }
  .icon { width: 24px; height: 24px; fill: var(--leaf); }
  .icon--person { width: 28px; height: 34px; margin-bottom: 10px; }
  .contact__name {
    font-size: 38px;
    font-weight: 300;
    line-height: 1.1;
  }
  .contact__name .surname { color: var(--leaf); }
  .contact__role {
    font-size: 14px;
    font-weight: 400;
    margin-top: 6px;
    color: #444;
  }
  .contact__phone-icon { margin-top: 34px; }
  .contact__phone {
    font-size: 25px;
    font-weight: 300;
    margin-top: 10px;
    letter-spacing: 0.01em;
  }
  .contact__mail-icon { margin-top: 30px; width: 22px; height: 16px; }
  .contact__email {
    font-size: 14px;
    font-weight: 400;
    margin-top: 8px;
  }
</style>
</head>
<body>
  <main class="sheet">
    <!-- Front side -->
    <section class="card card--front" aria-label="Card front">
      <div class="brand">
        <div class="brand__dot"></div>
        <p class="brand__name"><span>Verdant</span><span>Terraces</span></p>
      </div>
    </section>

    <!-- Back side -->
    <section class="card card--back" aria-label="Card back">
      <div class="card__band">
        <div class="brand">
          <div class="brand__dot"></div>
          <p class="brand__name"><span>Verdant</span><span>Terraces</span></p>
        </div>
      </div>

      <div class="contact">
        <svg class="icon icon--person" viewBox="0 0 28 34" aria-hidden="true">
          <circle cx="14" cy="9" r="7"/>
          <path d="M1 34 C1 23 6 18 14 18 C22 18 27 23 27 34 Z"/>
        </svg>
        <h1 class="contact__name">Owen <span class="surname">Harlow</span></h1>
        <p class="contact__role">Managing Director / Horticulturist</p>

        <svg class="icon contact__phone-icon" viewBox="0 0 24 24" aria-hidden="true">
          <path d="M6.6 10.8c1.4 2.8 3.8 5.2 6.6 6.6l2.2-2.2c.3-.3.7-.4 1-.2 1.1.4 2.3.6 3.6.6.6 0 1 .4 1 1V20c0 .6-.4 1-1 1C10.6 21 3 13.4 3 4c0-.6.4-1 1-1h3.5c.6 0 1 .4 1 1 0 1.3.2 2.5.6 3.6.1.3 0 .7-.2 1l-2.3 2.2z"/>
        </svg>
        <p class="contact__phone">0481 526 704</p>

        <svg class="icon contact__mail-icon" viewBox="0 0 22 16" aria-hidden="true">
          <path d="M0 0h22v16H0z M1.5 1.5 11 9l9.5-7.5" fill="var(--leaf)"/>
          <path d="M1.5 1.5 11 9l9.5-7.5" fill="none" stroke="#fff" stroke-width="1.4"/>
        </svg>
        <p class="contact__email">owenharlow@verdantterraces.com.au</p>
      </div>
    </section>
  </main>
</body>
</html>
```